Business Card Design Project

Same as the logo requirements.
Address of the store is:
Milo's Junction, LLC
287B North Linden Ave Suite 4
Warren, OH 44697
Gerald Pemberton, Owner
Updates

Project Deadline Extended
Reason: The design of the business cards should be the same as the main logo.

Project Deadline Extended
Reason: I approved the wrong design!

This is the link to the current logo design: http://files.artbinhub.net/img_store/273915/604128/604128_9275031_273915_pic.jpg

Target Market(s)

Courthouse and downtown employees, including lawyers, judges, downtown office workers.

Industry/Entity Type

Store

Font styles to use
Serif

Requirements
Must have
• Milo's Junction
A Corner Market, and Beyond, by Lantern Plaza!
Warren, OH 44697
Nice to have
• Colorful, Arrow sign

```html
<!DOCTYPE html>
<html lang="en">
<head>
<meta charset="utf-8">
<title>Milo's Junction – Business Card</title>
<link rel="stylesheet" href="https://fonts.googleapis.com/css2?family=Cinzel:wght@400;600&family=Lato:wght@300&family=PT+Sans:wght@700&display=swap">
<style>
  :root {
    --ink: #2a2a2a;
    --paper: #ffffff;
    --navy: #243846;
    --teal: #2ea68a;
    --mustard: #e9c042;
    --orange: #d9682c;
    --red: #d73030;
    --olive: #aec160;
    --edge: #1a1a1a;
  }
  html, body {
    margin: 0;
    padding: 0;
    width: 951px;
    height: 1200px;
    overflow: hidden;
    background: var(--paper);
  }
  .sheet {
    position: relative;
    width: 951px;
    height: 1200px;
  }
  .card {
    position: absolute;
    background: var(--paper);
    border: 1.5px solid var(--edge);
    box-sizing: border-box;
    overflow: hidden;
  }
  .card--front { left: 29px; top: 30px; width: 881px; height: 551px; }
  .card--back  { left: 41px; top: 610px; width: 880px; height: 550px; }

  .wordmark {
    position: absolute;
    margin: 0;
    font-family: "PT Sans", sans-serif;
    font-weight: 700;
    color: var(--ink);
    text-align: center;
    line-height: 0.82;
    letter-spacing: -0.01em;
    text-transform: uppercase;
  }
  .card--front .wordmark {
    left: 0; right: 0; top: 214px;
    font-size: 80px;
  }
  .card--back .wordmark {
    left: 0; width: 407px; top: 238px;
    font-size: 60px;
  }

  .front-url {
    position: absolute;
    left: 0; right: 0; top: 500px;
    margin: 0;
    padding-left: 0.5em;
    text-align: center;
    font-family: "Lato", sans-serif;
    font-weight: 300;
    font-size: 26px;
    line-height: 1;
    letter-spacing: 0.5em;
    color: var(--ink);
    transform: translateY(-32px);
  }
  .stripe {
    position: absolute;
    left: 0; right: 0; bottom: 0;
    height: 32px;
    display: flex;
  }
  .stripe span { display: block; height: 100%; }

  .contact-panel {
    position: absolute;
    left: 407px; top: 0;
    width: 473px; height: 100%;
    display: flex;
    flex-direction: column;
  }
  .contact-row {
    position: relative;
    height: 80px;
    display: flex;
    align-items: center;
    color: var(--paper);
    font-family: "Cinzel", serif;
    font-weight: 600;
    font-size: 22px;
    line-height: 1.25;
  }
  .contact-row .icon {
    position: absolute;
    left: 30px;
    width: 28px; height: 28px;
  }
  .contact-row .value { margin-left: 78px; }
  .identity {
    height: 150px;
    background: var(--navy);
    color: var(--paper);
    font-family: "Cinzel", serif;
    box-sizing: border-box;
    padding: 48px 0 0 30px;
  }
  .identity__name { margin: 0; font-size: 38px; font-weight: 400; line-height: 1; }
  .identity__role { margin: 2px 0 0; font-size: 23px; font-weight: 400; }

  .bg-navy { background: var(--navy); }
  .bg-teal { background: var(--teal); }
  .bg-mustard { background: var(--mustard); }
  .bg-orange { background: var(--orange); }
  .bg-red { background: var(--red); }
  .bg-olive { background: var(--olive); }
</style>
</head>
<body>
<main class="sheet">

  <section class="card card--front">
    <h1 class="wordmark">Milo’s<br>Junction</h1>
    <p class="front-url">www.milosjunction.com</p>
    <div class="stripe">
      <span class="bg-navy" style="width:135px"></span>
      <span class="bg-teal" style="width:152px"></span>
      <span class="bg-mustard" style="width:152px"></span>
      <span class="bg-orange" style="width:153px"></span>
      <span class="bg-red" style="width:152px"></span>
      <span class="bg-olive" style="flex:1"></span>
    </div>
  </section>

  <section class="card card--back">
    <h2 class="wordmark">Milo’s<br>Junction</h2>

    <div class="contact-panel">
      <div class="identity">
        <p class="identity__name">Gerald Pemberton</p>
        <p class="identity__role">Owner</p>
      </div>

      <div class="contact-row bg-teal">
        <svg class="icon" viewBox="0 0 28 28" aria-hidden="true">
          <path d="M14 1a9 9 0 0 0-9 9c0 6 9 17 9 17s9-11 9-17a9 9 0 0 0-9-9z" fill="#fff"/>
          <circle cx="14" cy="10" r="4" fill="var(--teal)"/>
          <circle cx="14" cy="10" r="2" fill="#fff"/>
        </svg>
        <span class="value">287B North Linden Ave Suite 4<br>Warren, OH 44697</span>
      </div>

      <div class="contact-row bg-mustard">
        <svg class="icon" viewBox="0 0 28 28" aria-hidden="true">
          <path d="M6 3l5 0 2 6-3 2c1.5 3 3.5 5 7 7l2-3 6 2v5l-3 3C12 24 4 16 3 6z" fill="#fff"/>
        </svg>
        <span class="value">+11 111 11 111</span>
      </div>

      <div class="contact-row bg-orange">
        <svg class="icon" viewBox="0 0 28 28" aria-hidden="true">
          <rect x="1" y="7" width="26" height="16" fill="#fff"/>
          <path d="M1 7l13 10L27 7M1 23l10-8M27 23l-10-8" stroke="var(--orange)" stroke-width="1.8" fill="none"/>
        </svg>
        <span class="value">gerald@milosjunction.com</span>
      </div>

      <div class="contact-row bg-red">
        <svg class="icon" viewBox="0 0 28 28" aria-hidden="true">
          <g fill="none" stroke="#fff" stroke-width="1.8">
            <circle cx="14" cy="14" r="11"/>
            <ellipse cx="14" cy="14" rx="5" ry="11"/>
            <path d="M3 14h22M5 8h18M5 20h18M14 3v22"/>
          </g>
        </svg>
        <span class="value">www.milosjunction.com</span>
      </div>

      <div class="contact-row bg-olive">
        <svg class="icon" viewBox="0 0 28 28" aria-hidden="true">
          <circle cx="14" cy="14" r="12" fill="#fff"/>
        </svg>
        <span class="value">geraldpemberton7773</span>
      </div>
    </div>
  </section>

</main>
</body>
</html>
```